Beautiful design for wordpress

I need a beautiful, colourful and feminine website. My business is called 'The Velvet Lantern', and I sell crystals, books, CD's, pendulums and other metaphysical items. I also provide Reiki (energy healing).
I want this design to be eye catching and inspire happiness and joy in those who see it. And I would love to see the use of the logo and its colours :)
Please add these on the web design: Home, About, Online store, Blog

Must have
• Colourful and playful, must use the logo somewhere, have the words on a menu saying 'Home, Blog, Online store and about' (or similar to those)And the design must stand out!
Should not have
• grey, brown and other boring colours.

```html
<!DOCTYPE html>
<html lang="en">
<head>
<meta charset="utf-8">
<title>The Velvet Lantern</title>
<link rel="stylesheet" href="https://fonts.googleapis.com/css2?family=Yesteryear&display=swap">
<style>
  :root {
    --bg: #4e2b17;
    --home: #fdaed3;
    --home-text: #e8aacb;
    --about: #fdcba8;
    --about-text: #ecc3a9;
    --store: #fdeca6;
    --store-text: #fcea9f;
    --blog: #c7e9b2;
    --blog-text: #bde3a3;
    --icon: #4e2b17;
    --badge: #ffffff;
    --brand: #7b7a76;
  }
  * { margin: 0; padding: 0; box-sizing: border-box; }
  html, body { width: 1200px; height: 873px; overflow: hidden; background: var(--bg); }
  .page { position: relative; width: 1200px; height: 873px; background: var(--bg); }
  .main-nav { position: absolute; inset: 0; }
  .nav-item {
    position: absolute; top: 28px; width: 200px; margin-left: -100px;
    display: flex; flex-direction: column; align-items: center;
    text-decoration: none;
  }
  .nav-label {
    font-family: "Yesteryear", cursive;
    font-size: 72px; line-height: 84px; height: 92px;
  }
  .nav-icon {
    width: 145px; height: 145px; border-radius: 50%;
    display: flex; align-items: center; justify-content: center;
  }
  .nav-icon svg { width: 90px; height: 90px; }
  .nav-home { left: 193px; }
  .nav-home .nav-label { color: var(--home-text); }
  .nav-home .nav-icon { background: var(--home); }
  .nav-about { left: 469px; }
  .nav-about .nav-label { color: var(--about-text); }
  .nav-about .nav-icon { background: var(--about); }
  .nav-store { left: 745px; }
  .nav-store .nav-label { color: var(--store-text); }
  .nav-store .nav-icon { background: var(--store); }
  .nav-blog { left: 1021px; }
  .nav-blog .nav-label { color: var(--blog-text); }
  .nav-blog .nav-icon { background: var(--blog); }

  .brand-badge {
    position: absolute; left: 361px; top: 308px;
    width: 472px; height: 472px; border-radius: 50%;
    background: var(--badge);
    display: flex; align-items: center; justify-content: center;
  }
  .brand-name {
    font-family: "Yesteryear", cursive;
    font-size: 64px; line-height: 1.05; text-align: center;
    color: var(--brand);
  }
</style>
</head>
<body>
<div class="page">
  <nav class="main-nav">
    <a class="nav-item nav-home" href="#">
      <span class="nav-label">Home</span>
      <span class="nav-icon">
        <svg viewBox="0 0 90 90" aria-hidden="true">
          <path d="M20 40 Q20 14 45 14 Q70 14 70 40 L62 40 L66 76 L52 76 Q52 58 45 58 Q38 58 38 76 L24 76 L28 40 Z" fill="var(--icon)"/>
          <circle cx="45" cy="32" r="7" fill="var(--home)"/>
          <path d="M45 25 V39 M38 32 H52" stroke="var(--icon)" stroke-width="2"/>
        </svg>
      </span>
    </a>
    <a class="nav-item nav-about" href="#">
      <span class="nav-label">About</span>
      <span class="nav-icon">
        <svg viewBox="0 0 90 90" aria-hidden="true">
          <path d="M30 30 Q30 14 46 14 Q62 14 62 30 Q62 40 52 46 Q46 50 46 60" fill="none" stroke="var(--icon)" stroke-width="6" stroke-linecap="round"/>
          <circle cx="33" cy="31" r="5" fill="var(--icon)"/>
          <circle cx="46" cy="74" r="5" fill="var(--icon)"/>
        </svg>
      </span>
    </a>
    <a class="nav-item nav-store" href="#">
      <span class="nav-label">Store</span>
      <span class="nav-icon">
        <svg viewBox="0 0 90 90" aria-hidden="true">
          <path d="M20 44 Q22 14 45 14 Q68 14 70 44" fill="none" stroke="var(--icon)" stroke-width="7"/>
          <path d="M10 40 H80 L74 76 Q72 80 68 80 H22 Q18 80 16 76 Z" fill="var(--icon)"/>
          <g fill="var(--store)">
            <rect x="24" y="50" width="8" height="7"/><rect x="36" y="50" width="8" height="7"/><rect x="48" y="50" width="8" height="7"/><rect x="60" y="50" width="8" height="7"/>
            <rect x="26" y="62" width="8" height="7"/><rect x="38" y="62" width="8" height="7"/><rect x="50" y="62" width="8" height="7"/><rect x="62" y="62" width="6" height="7"/>
          </g>
        </svg>
      </span>
    </a>
    <a class="nav-item nav-blog" href="#">
      <span class="nav-label">Blog</span>
      <span class="nav-icon">
        <svg viewBox="0 0 90 90" aria-hidden="true">
          <path d="M48 14 C72 14 84 28 82 44 C80 60 64 68 46 66 C36 66 30 64 26 62 L8 76 L16 58 C8 50 10 36 18 26 C26 18 36 14 48 14 Z" fill="var(--icon)"/>
          <path d="M48 22 C66 22 76 32 74 44 C72 56 60 60 46 58 C34 58 24 54 20 46 C18 34 30 22 48 22 Z" fill="var(--blog)"/>
        </svg>
      </span>
    </a>
  </nav>

  <div class="brand-badge">
    <h1 class="brand-name">The Velvet<br>Lantern</h1>
  </div>
</div>
</body>
</html>
```